Quarrow Construction Limited needs a complete stationary

We need a complete stationary based on our attached logo. Stationary should be need and clean with some simple high class design. We are targeting global customers to serve construction work, manpower supply and equipment supply services. We believe in quality work, reasonable cost and on time delivery. Our all stationary should be match with our business nature.

Target Market(s)

word wide

Industry/Entity Type

Construction Company

Font styles to use
Sans Serif

Requirements
Must have
• Good looking, clean type and simple design
Nice to have
• any good design any good font
Should not have
• rough design

```html
<!DOCTYPE html>
<html lang="en">
<head>
<meta charset="utf-8">
<title>Quarrow Construction Limited — Stationery</title>
<link href="https://fonts.googleapis.com/css2?family=Roboto:wght@400;500;700&family=Roboto+Condensed:wght@400&display=swap" rel="stylesheet">
<style>
  :root{
    --blue:#0f4f9e;
    --blue-light:#8aaedb;
    --paper:#ffffff;
    --ink:#1b1b1b;
    --board:#c9c9c9;
    --watermark:#e3eaf4;
    --shadow:6px 9px 10px rgba(0,0,0,.45);
  }
  *{box-sizing:border-box;margin:0;padding:0}
  html,body{width:1200px;height:1200px;overflow:hidden;background:var(--board)}
  .board{position:relative;width:1200px;height:1200px;font-family:"Roboto Condensed",sans-serif;color:var(--ink)}

  .card{position:absolute;width:270px;height:154px;background:var(--paper);box-shadow:var(--shadow);overflow:hidden}
  .col-1{left:93px}.col-2{left:446px}.col-3{left:798px}
  .row-1{top:40px}.row-2{top:219px}.row-3{top:398px}

  .mark{position:absolute;width:var(--d);height:var(--d);border-radius:50%;background:var(--paper);
        border:calc(var(--d)*0.04) solid var(--blue);display:flex;align-items:center;justify-content:center;
        transform:translate(-50%,-50%)}
  .mark-name{font-family:"Roboto",sans-serif;font-weight:700;color:var(--blue);font-size:calc(var(--d)*0.19);letter-spacing:.02em}
  .mark.faint{border-color:var(--watermark);background:transparent}
  .mark.faint .mark-name{color:var(--watermark)}

  .person{position:absolute;font-family:"Roboto",sans-serif}
  .person .name{font-weight:500;font-size:12px;color:var(--blue);line-height:1}
  .person .role{font-family:"Roboto Condensed",sans-serif;font-size:7.5px;margin-top:5px;color:var(--ink)}
  .person.right{text-align:right}
  .on-blue .name,.on-blue .role,.on-blue .contact,.on-blue .address{color:#fff}

  .contact{position:absolute;font-size:8.5px;line-height:11px;color:var(--ink)}
  .contact li{list-style:none;display:flex;align-items:center;gap:5px;white-space:nowrap}
  .contact li.gap{margin-top:4px}
  .contact svg{width:7px;height:7px;fill:currentColor;flex:none}
  .contact .address{color:var(--blue);font-size:9px;line-height:11px;margin-top:8px}
  .on-blue .contact .address{color:#fff}

  .divider{position:absolute;width:1px;background:var(--blue)}

  .c1 .band{position:absolute;left:0;top:0;width:100%;height:83px;background:var(--blue)}
  .c4 .band{position:absolute;left:0;bottom:0;width:100%;height:19px;background:var(--blue)}
  .c6 .band{position:absolute;left:0;top:79px;width:100%;height:75px;background:var(--blue)}
  .c8{background:var(--blue)}
  .c9 .panel{position:absolute;left:0;top:0;width:122px;height:100%;background:var(--blue)}
  .swoosh{position:absolute;left:0;width:100%}

  .envelope{position:absolute;left:110px;width:506px;height:228px;background:var(--paper);box-shadow:var(--shadow);overflow:hidden}
  .envelope.front{top:652px}
  .envelope.back{top:914px}
  .envelope .return{position:absolute;left:21px;top:71px;font-size:7px;line-height:8px}
  .flap{position:absolute;left:0;top:0;width:506px;height:58px}

  .letterhead{position:absolute;left:694px;top:598px;width:398px;height:564px;background:var(--paper);box-shadow:var(--shadow);overflow:hidden}
  .letterhead .contact{font-size:5px;line-height:6.5px}
  .letterhead .contact svg{width:4px;height:4px}
  .letterhead .contact li{gap:3px}
  .letterhead .contact li.gap{margin-top:3px}
  .letterhead .contact .address{font-size:5px;line-height:6px;margin-top:3px}
</style>
</head>
<body>
<svg width="0" height="0" style="position:absolute" aria-hidden="true">
  <symbol id="i-phone" viewBox="0 0 10 10"><path d="M1 4 Q5 0 9 4 L8 5 L6.5 4 L6.5 3.3 Q5 2.8 3.5 3.3 L3.5 4 L2 5 Z M2.5 5 L7.5 5 L8.5 9 L1.5 9 Z"/></symbol>
  <symbol id="i-fax" viewBox="0 0 10 10"><path d="M3 0 H7 V3 H3 Z M1 3.5 H9 V9 H1 Z" /></symbol>
  <symbol id="i-mail" viewBox="0 0 10 10"><path d="M0 2 H10 V9 H0 Z M0.8 2.6 L5 6 L9.2 2.6 Z" fill-rule="evenodd"/></symbol>
  <symbol id="i-web" viewBox="0 0 10 10"><path d="M5 0.5 A4.5 4.5 0 1 0 5.01 0.5 Z M5 1.5 A3.5 3.5 0 1 1 4.99 1.5 Z M1 4.5 H9 V5.5 H1 Z M4.5 1 H5.5 V9 H4.5 Z" fill-rule="evenodd"/></symbol>
</svg>

<main class="board">

  <section class="card c1 col-1 row-1">
    <div class="band"></div>
    <div class="mark" style="--d:84px;left:67px;top:82px"><span class="mark-name">Quarrow</span></div>
    <div class="person on-blue" style="left:137px;top:46px"><div class="name">Marcus Reyland</div><div class="role">Director</div></div>
    <ul class="contact" style="left:137px;top:95px">
      <li><svg><use href="#i-phone"/></svg>(000) 555-0140</li>
      <li><svg><use href="#i-fax"/></svg>(000) 555-0172</li>
      <li class="gap"><svg><use href="#i-mail"/></svg>info@quarrowbuild.com</li>
      <li><svg><use href="#i-web"/></svg>www.quarrowbuild.com</li>
    </ul>
  </section>

  <section class="card c2 col-2 row-1">
    <svg class="swoosh" style="top:0;height:42px" viewBox="0 0 270 42" preserveAspectRatio="none">
      <path d="M0 0 H270 V16 Q200 8 150 12 Q60 18 0 42 Z" fill="var(--blue-light)"/>
      <path d="M0 0 H270 V16 Q210 10 150 11 Q60 14 0 22 Z" fill="var(--blue)"/>
    </svg>
    <div class="person right" style="right:164px;top:61px"><div class="name">Marcus Reyland</div><div class="role">Director</div></div>
    <div class="divider" style="left:127px;top:60px;height:79px"></div>
    <ul class="contact" style="left:143px;top:60px">
      <li><svg><use href="#i-phone"/></svg>(000) 555-0140</li>
      <li><svg><use href="#i-fax"/></svg>(000) 555-0172</li>
      <li class="gap"><svg><use href="#i-mail"/></svg>info@quarrowbuild.com</li>
      <li><svg><use href="#i-web"/></svg>www.quarrowbuild.com</li>
      <li class="address">118 Ridgeline Ave<br>City Name, Address line</li>
    </ul>
  </section>

  <section class="card c3 col-3 row-1">
    <div class="mark" style="--d:84px;left:135px;top:77px"><span class="mark-name">Quarrow</span></div>
  </section>

  <section class="card c4 col-1 row-2">
    <div class="band"></div>
    <div class="person right" style="right:160px;top:37px"><div class="name">Marcus Reyland</div><div class="role">Director</div></div>
    <div class="divider" style="left:129px;top:33px;height:82px"></div>
    <ul class="contact" style="left:141px;top:34px">
      <li><svg><use href="#i-phone"/></svg>(000) 555-0140</li>
      <li><svg><use href="#i-fax"/></svg>(000) 555-0172</li>
      <li class="gap"><svg><use href="#i-mail"/></svg>info@quarrowbuild.com</li>
      <li><svg><use href="#i-web"/></svg>www.quarrowbuild.com</li>
      <li class="address">118 Ridgeline Ave<br>City Name, Address line</li>
    </ul>
  </section>

  <section class="card c5 col-2 row-2">
    <div class="mark" style="--d:58px;left:222px;top:42px"><span class="mark-name">Quarrow</span></div>
    <div class="person" style="left:17px;top:15px"><div class="name">Marcus Reyland</div><div class="role">Director</div></div>
    <ul class="contact" style="left:17px;top:57px">
      <li><svg><use href="#i-phone"/></svg>(000) 555-0140</li>
      <li><svg><use href="#i-fax"/></svg>(000) 555-0172</li>
      <li class="gap"><svg><use href="#i-mail"/></svg>info@quarrowbuild.com</li>
      <li><svg><use href="#i-web"/></svg>www.quarrowbuild.com</li>
      <li class="address">118 Ridgeline Ave<br>City Name, Address line</li>
    </ul>
    <svg class="swoosh" style="bottom:0;height:13px" viewBox="0 0 270 13" preserveAspectRatio="none">
      <rect x="0" y="0" width="270" height="13" fill="var(--blue)"/>
      <path d="M0 0 H170 Q185 2 193 13 H0 Z" fill="var(--blue-light)"/>
      <path d="M170 0 H178 Q190 3 198 13 H193 Q185 2 170 0 Z" fill="#fff"/>
    </svg>
  </section>

  <section class="card c6 col-3 row-2">
    <div class="band"></div>
    <div class="mark" style="--d:84px;left:135px;top:76px"><span class="mark-name">Quarrow</span></div>
  </section>

  <section class="card c7 col-1 row-3">
    <div class="mark" style="--d:48px;left:227px;top:36px"><span class="mark-name">Quarrow</span></div>
    <div class="person" style="left:17px;top:15px"><div class="name">Marcus Reyland</div><div class="role">Director</div></div>
    <ul class="contact" style="left:17px;top:57px">
      <li><svg><use href="#i-phone"/></svg>(000) 555-0140</li>
      <li><svg><use href="#i-fax"/></svg>(000) 555-0172</li>
      <li class="gap"><svg><use href="#i-mail"/></svg>info@quarrowbuild.com</li>
      <li><svg><use href="#i-web"/></svg>www.quarrowbuild.com</li>
      <li class="address">118 Ridgeline Ave<br>City Name, Address line</li>
    </ul>
    <svg class="swoosh" style="bottom:0;height:14px" viewBox="0 0 270 14" preserveAspectRatio="none">
      <rect x="0" y="0" width="270" height="14" fill="var(--blue)"/>
      <path d="M0 0 H172 L166 14 H0 Z" fill="var(--blue-light)"/>
      <path d="M172 0 H178 L172 14 H166 Z" fill="#fff"/>
    </svg>
  </section>

  <section class="card c8 col-2 row-3 on-blue">
    <div class="person" style="left:15px;top:15px"><div class="name">Marcus Reyland</div><div class="role">Director</div></div>
    <ul class="contact" style="left:17px;top:59px">
      <li><svg><use href="#i-phone"/></svg>(000) 555-0140</li>
      <li><svg><use href="#i-fax"/></svg>(000) 555-0172</li>
      <li class="gap"><svg><use href="#i-mail"/></svg>info@quarrowbuild.com</li>
      <li><svg><use href="#i-web"/></svg>www.quarrowbuild.com</li>
      <li class="address">118 Ridgeline Ave<br>City Name, Address line</li>
    </ul>
    <div class="mark" style="--d:84px;left:206px;top:94px"><span class="mark-name">Quarrow</span></div>
  </section>

  <section class="card c9 col-3 row-3">
    <div class="panel"></div>
    <div class="mark" style="--d:82px;left:61px;top:82px"><span class="mark-name">Quarrow</span></div>
    <div class="person" style="left:136px;top:14px"><div class="name">Marcus Reyland</div><div class="role">Director</div></div>
    <ul class="contact" style="left:136px;top:61px">
      <li><svg><use href="#i-phone"/></svg>(000) 555-0140</li>
      <li><svg><use href="#i-fax"/></svg>(000) 555-0172</li>
      <li class="gap"><svg><use href="#i-mail"/></svg>info@quarrowbuild.com</li>
      <li><svg><use href="#i-web"/></svg>www.quarrowbuild.com</li>
      <li class="address">118 Ridgeline Ave<br>City Name, Address line</li>
    </ul>
  </section>

  <section class="envelope front">
    <div class="mark" style="--d:52px;left:47px;top:40px"><span class="mark-name">Quarrow</span></div>
    <p class="return">118 Ridgeline Ave<br>City Name, Address line</p>
  </section>

  <section class="envelope back">
    <svg class="flap" viewBox="0 0 506 58" preserveAspectRatio="none">
      <path d="M0 0 H506 L460 48 Q450 58 436 58 H70 Q56 58 46 48 Z" fill="var(--blue)"/>
    </svg>
    <div class="mark" style="--d:40px;left:253px;top:29px"><span class="mark-name">Quarrow</span></div>
  </section>

  <section class="letterhead">
    <div class="mark" style="--d:66px;left:76px;top:57px"><span class="mark-name">Quarrow</span></div>
    <div class="divider" style="left:286px;top:32px;height:51px"></div>
    <ul class="contact" style="left:293px;top:34px">
      <li><svg><use href="#i-phone"/></svg>(000) 555-0140</li>
      <li><svg><use href="#i-fax"/></svg>(000) 555-0172</li>
      <li class="gap"><svg><use href="#i-mail"/></svg>info@quarrowbuild.com</li>
      <li><svg><use href="#i-web"/></svg>www.quarrowbuild.com</li>
      <li class="address">118 Ridgeline Ave<br>City Name, Address line</li>
    </ul>
    <div class="mark faint" style="--d:140px;left:200px;top:320px"><span class="mark-name">Quarrow</span></div>
  </section>

</main>
</body>
</html>
```